Business card for a plastic surgeon

i need a business card for a plastic surgeon. I have two adresses. The card should communicate safety, simmetry, beauty and with soft colors.
What i want in the card:
- my logo: Letters "R"and "B" (picture uploaded)
- my name: Renato Bastiani
- my registration: CRM 507 219
- my adresses and phone numbers (2):
- Av Dr Teixeira Lopes, 2710, sala 305 - Vila Olímpia | São Paulo/ SP - Phone: 11 4172-5036
- Al. Itapeva, 47, 3 andar - Alphaville | Barueri/ SP - Phone: 11 6350-2481

- my social network: site, facebook and instagram

Target Market(s)

people (95% girls and women) that want cosmetic procedures and plastic surgery

Industry/Entity Type

Business

Contact Information for Business Card

The card should communicate safety, simmetry, beauty and with soft colors.
Beige, brown, gray, rosy are some options. Color is free

Font styles to use
Serif

Requirements
Must have
• - my logo: Letters "R"and "B" (picture uploaded)
• - my name: Renato Bastiani
• - my registration: CRM 507 219
• - my adresses and phone numbers (2):
• - Av Dr Teixeira Lopes, 2710, sala 305 - Vila Olímpia | São Paulo/ SP - Phone: 11 4172-5036
• - Al. Itapeva, 47, 3 andar - Alphaville | Barueri/ SP - Phone: 11 6350-2481
• - my social network: site, facebook and instagram
Should not have
• other images (only my logo)

```html
<!DOCTYPE html>
<html lang="pt-BR">
<head>
<meta charset="UTF-8">
<title>Dr. Renato Bastiani – Cartão de Visita</title>
<link href="https://fonts.googleapis.com/css2?family=Cinzel:wght@400;500&family=EB+Garamond:wght@400;500&display=swap" rel="stylesheet">
<style>
  :root {
    --backdrop: #e6e4e1;
    --card-white: #ffffff;
    --ink: #1a1a1a;
    --band: #0e0d0d;
    --taupe: #a8927c;
    --taupe-dark: #8c7660;
    --shadow: rgba(0, 0, 0, 0.22);
  }
  * { box-sizing: border-box; margin: 0; padding: 0; }
  html, body {
    width: 1200px; height: 880px; overflow: hidden;
    background: var(--backdrop);
  }
  .canvas { position: relative; width: 1200px; height: 880px; }

  .card {
    position: absolute;
    width: 560px; height: 320px;
    border-radius: 22px;
    background: var(--card-white);
    box-shadow: 0 14px 34px var(--shadow);
    overflow: hidden;
  }

  /* Front */
  .card-front { left: 60px; top: 110px; }
  .front-content {
    position: absolute; inset: 0;
    display: flex; flex-direction: column; align-items: center; justify-content: center;
  }
  .monogram {
    font-family: "Cinzel", serif;
    font-size: 64px; font-weight: 400; color: var(--ink);
    letter-spacing: 4px; line-height: 1; margin-bottom: 18px;
  }
  .front-name {
    font-family: "Cinzel", serif;
    font-size: 30px; color: var(--ink); letter-spacing: 1px; line-height: 1;
  }
  .front-title {
    font-family: "Cinzel", serif;
    font-size: 13px; color: var(--ink); letter-spacing: 6px; margin-top: 6px;
  }
  .website {
    font-family: "EB Garamond", serif;
    font-size: 15px; color: var(--ink); margin-top: 24px;
  }
  .website .accent { color: var(--taupe); }

  /* Back */
  .card-back { left: 580px; top: 460px; }
  .back-band {
    position: absolute; left: 0; top: 0; width: 100%; height: 140px;
    background: var(--band);
    border-bottom: 9px solid var(--taupe);
  }
  .social {
    position: absolute; right: 22px; top: 18px;
    font-family: "EB Garamond", serif; font-size: 13px; color: var(--taupe);
    display: flex; align-items: center; gap: 6px;
  }
  .social .dot { width: 9px; height: 9px; background: var(--taupe); }
  .band-name {
    position: absolute; left: 30px; top: 62px;
    font-family: "Cinzel", serif; font-size: 30px; color: var(--taupe-dark); line-height: 1;
  }
  .band-title {
    position: absolute; left: 56px; top: 98px;
    font-family: "Cinzel", serif; font-size: 13px; color: var(--taupe-dark); letter-spacing: 6px;
  }
  .details {
    position: absolute; left: 30px; top: 160px; right: 20px;
    font-family: "EB Garamond", serif; color: var(--ink);
  }
  .details .person {
    font-family: "Cinzel", serif; font-size: 20px; color: var(--taupe); line-height: 1;
  }
  .details .crm { font-size: 15px; margin-bottom: 10px; }
  .address { font-size: 14px; line-height: 1.25; margin-bottom: 8px; }
  .address .label { color: var(--taupe); font-weight: 500; }
</style>
</head>
<body>
<main class="canvas">
  <section class="card card-front">
    <div class="front-content">
      <div class="monogram">RB</div>
      <div class="front-name">DR. RENATO BASTIANI</div>
      <div class="front-title">CIRURGIÃO PLÁSTICO</div>
      <div class="website">www.<span class="accent">bastianiclinica</span>.com</div>
    </div>
  </section>

  <section class="card card-back">
    <div class="back-band">
      <div class="social"><span class="dot"></span>@bastianiclinica</div>
      <div class="band-name">DR. RENATO BASTIANI</div>
      <div class="band-title">CIRURGIÃO PLÁSTICO</div>
    </div>
    <div class="details">
      <div class="person">RENATO BASTIANI</div>
      <div class="crm">CRM 507 219</div>
      <p class="address">Av Dr Teixeira Lopes, 2710, sala 305 - Vila Olímpia | São Paulo/ SP<br>
        <span class="label">P:</span> 11 4172-5036</p>
      <p class="address">Al. Itapeva, 47, 3 andar - Alphaville | Barueri/ SP<br>
        <span class="label">P:</span> 11 6350-2481</p>
    </div>
  </section>
</main>
</body>
</html>
```